Presentation Folder Design

We are a young and dynamic lettings agent in London and surround and we are looking for a fresh and stunning design for our A4 presentation folder. Our colors are shades of green. Our logo can be found on http://www.kelworthlets.co.uk

Please read the technical info below. It is very important to comply with the specs.

Thank you!
Updates

The design should contain 3 shades of green and the logo which will be emailed to you, clean lines, discreet skyline representing buildings.

Technical

Requirements
Must have
• Resolution 350 dpi. The resolution changes over 300 dpi are almost imperceptible so do not increase the resolution without need - it does not improve the quality but enlarges the file volume (size) instead.
Artwork dimentions: 521 x 364 mm. Use template for designing. Folders were designed to fit A4 paper. The easiest way is to download already made template. NOTE: Do not change the position of template toward paper sheet.
Color management Please provide your artwork in CMYK palette. Ensure that ALL images, text and other design elements have colors set to CMYK palette and do not contain any RGB or Pantone colors.
Acceptable file types PDF (ver. 1.4 max) PSD CDR (ver. X3 max) TIF JPG
Maximum percentage of the process inks Cannot exceed : 350%. Complaints about artworks with higher ink coverage will not be accepted (so e.g. do not "deep black" using 100+100+100+100% of CMYK colors).
Deep black: In order to obtain rich saturated black use 84%C 74%M 62%Y 100%K.

```html
<!DOCTYPE html>
<html lang="en">
<head>
<meta charset="utf-8">
<title>Kelworth Lettings – Presentation Folder Cover</title>
<link rel="stylesheet" href="https://fonts.googleapis.com/css2?family=Open+Sans:wght@700;800&display=swap">
<style>
  :root {
    --stage: #dfe5e8;
    --paper: #f2f4ee;
    --green-dark: #1f4a2a;
    --green-mid: #4f8a1f;
    --green-bright: #3f9e2e;
    --green-light: #c6d196;
    --green-pale: #dde4bd;
    --white: #ffffff;
  }
  html, body {
    margin: 0;
    width: 1200px;
    height: 857px;
    overflow: hidden;
    background: var(--stage);
    font-family: "Open Sans", Arial, sans-serif;
  }
  .canvas {
    position: relative;
    width: 1200px;
    height: 857px;
  }
  .folder-cover {
    position: absolute;
    left: 330px;
    top: 48px;
    width: 540px;
    height: 760px;
    background: var(--paper);
    box-shadow: 0 6px 24px rgba(30, 50, 40, 0.18);
    overflow: hidden;
  }
  .cover-graphics {
    position: absolute;
    inset: 0;
  }
  .brand {
    position: absolute;
    left: 124px;
    top: 172px;
    display: flex;
    align-items: center;
    gap: 12px;
  }
  .brand-name {
    font-weight: 800;
    font-size: 46px;
    letter-spacing: -1px;
    color: var(--green-bright);
    line-height: 1;
  }
  .brand-square {
    width: 22px;
    height: 22px;
    background: var(--green-mid);
  }
  .service-label {
    position: absolute;
    left: 124px;
    top: 262px;
    padding: 8px 26px;
    background: var(--green-dark);
    color: var(--white);
    font-weight: 700;
    font-size: 26px;
    letter-spacing: 1px;
    line-height: 1.2;
  }
</style>
</head>
<body>
<main class="canvas">
  <section class="folder-cover" aria-label="Kelworth Lettings folder front cover">
    <svg class="cover-graphics" width="540" height="760" viewBox="0 0 540 760" aria-hidden="false">
      <!-- skyline area -->
      <rect class="skyline" x="112" y="380" width="360" height="262" fill="url(#skylineTone)" role="img" aria-label="Discreet city skyline of London buildings in soft olive green"/>
      <defs>
        <linearGradient id="skylineTone" x1="0" y1="0" x2="0" y2="1">
          <stop offset="0" stop-color="#dde4bd"/>
          <stop offset="1" stop-color="#c6d196"/>
        </linearGradient>
      </defs>

      <!-- vertical bands -->
      <rect class="band-vertical-light" x="62" y="0" width="8" height="760" fill="var(--green-light)"/>
      <rect class="band-vertical-dark" x="74" y="0" width="10" height="760" fill="var(--green-dark)"/>
      <rect class="band-vertical-mid" x="88" y="0" width="20" height="760" fill="var(--green-mid)"/>

      <!-- horizontal bands -->
      <rect class="band-horizontal-light" x="0" y="578" width="540" height="8" fill="var(--green-light)"/>
      <rect class="band-horizontal-dark" x="0" y="590" width="540" height="12" fill="var(--green-dark)"/>
      <rect class="band-horizontal-mid" x="0" y="606" width="540" height="20" fill="var(--green-mid)"/>

      <!-- arrow marks at band ends -->
      <g class="arrow-marks-top" fill="var(--green-mid)">
        <polygon points="70,22 86,10 102,22 102,28 86,16 70,28"/>
        <polygon points="70,34 86,22 102,34 102,40 86,28 70,40"/>
      </g>
      <g class="arrow-marks-side" fill="var(--green-mid)">
        <polygon points="506,582 518,596 506,610 500,610 512,596 500,582"/>
        <polygon points="518,582 530,596 518,610 512,610 524,596 512,582"/>
      </g>
    </svg>

    <div class="brand">
      <span class="brand-name">kelworth</span>
      <span class="brand-square"></span>
    </div>
    <div class="service-label">LETTINGS</div>
  </section>
</main>
</body>
</html>
```